Marlow Crest Holdings (Remodeling company) needs a logo and business card

We need a business card design for a new company. We "flip" upmarket houses (buy, remodel and sell) in the Austin, TX area. I'd like neutral colors (grey, white, gold black). I would like it to include a simple, clean logo. Our designs are modern and uncluttered and I would like that reflected in the business card design.

Target Market(s)

Young professionals, Families, Retirees. Our properties will sell for $750k+

Industry/Entity Type

Real Estate

Contact Information for Business Card

Marlow Crest Holdings
Nora Pellham
(555) 216 7042
Owner
Rory Tansil
(555) 638 1975
Realtor

Logo Text

Marlow Crest Holdings

Font styles to use
Serif
Script

Requirements
Must have
• Simple, classic design
Nice to have
• Clean lines, modern look
Should not have
• Too traditionally

```html
<!DOCTYPE html>
<html lang="en">
<head>
<meta charset="utf-8">
<title>Marlow Crest Holdings — Business Cards</title>
<link rel="stylesheet" href="https://fonts.googleapis.com/css2?family=Montserrat:wght@400;500;600&display=swap">
<style>
  :root {
    --bg: #2a2a2b;
    --card: #0b0b0b;
    --card-edge: #1a1a1a;
    --gold: #d6b43c;
    --gold-soft: #c9a632;
  }
  html, body {
    margin: 0;
    padding: 0;
    width: 1200px;
    height: 900px;
    overflow: hidden;
    background: var(--bg);
  }
  .canvas {
    width: 1200px;
    height: 900px;
    display: flex;
    flex-direction: column;
    align-items: center;
    justify-content: center;
    gap: 48px;
  }
  .card {
    position: relative;
    width: 640px;
    height: 366px;
    background: linear-gradient(160deg, #141414 0%, var(--card) 60%);
    border: 1px solid var(--card-edge);
    box-sizing: border-box;
    font-family: "Montserrat", sans-serif;
    color: var(--gold);
  }
  .card-frame {
    position: absolute;
    inset: 28px;
    border: 2px solid var(--gold);
  }
  .brand-name {
    position: absolute;
    top: 112px;
    left: 0;
    right: 0;
    text-align: center;
    font-weight: 600;
    font-size: 30px;
    letter-spacing: 0.5px;
    color: var(--gold);
    margin: 0;
  }
  .contact-phone {
    position: absolute;
    top: 200px;
    right: 80px;
    font-size: 14px;
    font-weight: 500;
    letter-spacing: 0.6px;
    color: var(--gold-soft);
    margin: 0;
  }
  .contact-person {
    position: absolute;
    top: 262px;
    left: 86px;
    font-size: 14px;
    font-weight: 500;
    letter-spacing: 0.6px;
    color: var(--gold-soft);
    margin: 0;
  }
</style>
</head>
<body>
  <main class="canvas">
    <article class="card card--owner">
      <div class="card-frame"></div>
      <p class="brand-name">Marlow Crest Holdings</p>
      <p class="contact-phone">Phone : (555) 216 7042</p>
      <p class="contact-person">Nora Pellham | Owner</p>
    </article>
    <article class="card card--realtor">
      <div class="card-frame"></div>
      <p class="brand-name">Marlow Crest Holdings</p>
      <p class="contact-phone">Phone : (555) 638 1975</p>
      <p class="contact-person">Rory Tansil | Realtor</p>
    </article>
  </main>
</body>
</html>
```